Abia Investment Brochure for investment promotion

We need an investment manual to sell the potential of Abia state (a state in Nigeria) to investors around the world. This manual / brochure should be top class and have a premium feel.

We have developed the content as attached and all that is required is to fit the content into a brochure format.
The brochure should be top class, easy to read and very friendly to investors

Target Market(s)

World Investors

Industry/Entity Type

Investment

Requirements
Must have
• Abia State Logo (Can find online), Kelmor Tower (can find online). Premium feel and look. design should be clean, no clutter. General images that represent investment sectors
Nice to have
• Pictures
Should not have
• Images of white men.

```html
<!DOCTYPE html>
<html lang="en">
<head>
<meta charset="utf-8">
<title>Invest in Abia – Welcome</title>
<link rel="stylesheet" href="https://fonts.googleapis.com/css2?family=Open+Sans:wght@400;600&family=Tinos:wght@700&display=swap">
<style>
  :root {
    --page: #ffffff;
    --forest: #0f4d2b;
    --gold: #b8954a;
    --gold-plate: #b99553;
    --gold-plate-light: #c9a866;
    --ink: #2a2a2a;
    --plate-ink: #1f2a1a;
    --portrait-light: #d6c49a;
    --portrait-dark: #b89f6c;
  }
  * { margin: 0; padding: 0; box-sizing: border-box; }
  html, body { width: 849px; height: 1200px; overflow: hidden; background: var(--page); }
  .page {
    position: relative;
    width: 849px;
    height: 1200px;
    background: var(--page);
    font-family: "Open Sans", sans-serif;
  }
  .portrait {
    position: absolute;
    left: 192px;
    top: 42px;
    width: 476px;
    height: 586px;
  }
  .portrait-photo {
    position: absolute;
    inset: 0 0 62px 0;
    background: linear-gradient(160deg, var(--portrait-light), var(--portrait-dark));
  }
  .name-plate {
    position: absolute;
    left: 0; right: 0; bottom: 0;
    height: 62px;
    background: linear-gradient(180deg, var(--gold-plate-light), var(--gold-plate));
    padding: 8px 0 0 30px;
    color: var(--plate-ink);
    font-family: "Tinos", serif;
  }
  .name-plate .name { font-size: 27px; font-weight: 700; letter-spacing: 1px; line-height: 1; }
  .name-plate .name sup { font-size: 11px; letter-spacing: 0; }
  .name-plate .title { font-size: 16px; font-weight: 700; letter-spacing: 0.5px; margin-top: 4px; }
  .pledge {
    position: absolute;
    top: 738px;
    left: 0; right: 0;
    text-align: center;
    color: var(--gold);
    font-size: 27px;
    line-height: 1.3;
  }
  .outline-band {
    position: absolute;
    left: 0;
    top: 962px;
    width: 815px;
    height: 46px;
    background: var(--forest);
  }
  .outline-band h2 {
    position: absolute;
    left: 410px;
    top: 6px;
    color: #fff;
    font-weight: 400;
    font-size: 26px;
  }
  .outline-list {
    position: absolute;
    left: 410px;
    top: 1022px;
    list-style: none;
    color: var(--ink);
    font-size: 16px;
  }
  .outline-list li { line-height: 32px; }
</style>
</head>
<body>
<main class="page">
  <figure class="portrait">
    <div class="portrait-photo" role="img" aria-label="Official portrait photograph of the state governor"></div>
    <div class="name-plate">
      <div class="name">EMEKA NWOSU <sup>Ph.D</sup></div>
      <div class="title">GOVERNOR OF ABIA STATE</div>
    </div>
  </figure>

  <p class="pledge">“We fully commit to a friendly and<br>unrivaled business environment<br>for your investment”</p>

  <section class="outline-band"><h2>Outline</h2></section>
  <ul class="outline-list">
    <li>Welcome to Abia</li>
    <li>Why Abia is suitable for Investment</li>
    <li>Investment Opportunities</li>
    <li>Getting Started</li>
  </ul>
</main>
</body>
</html>
```